Lantern CD Jacket - BSC Worship Album

Album Name: Lantern | Artist: BSC Worship

We need a CD Jacket with these items:
1. Front Cover design to be displayed on Sonora, Playvio, etc.
2. Back Cover design with song titles and production info
3. Insert Sheet design containing All Lyrics and Credit Title
4. CD Plate design

The final design should communicate a commitment to be like our Lord Jesus Christ in an abstract / subtle way.

Lantern meaning: Two or more subjects similar to each other.

This is the theme song lyrics to summarized the meaning:
LANTERN // Great is the Lord God almighty / Your Kingdom come, Your will be done // Great is the Lord God almighty / You saved my life, You give me hope // And through it all / With all I am // Lantern... I will shine like You Jesus / Your love and Your grace live in me / Lantern... I will live like You Jesus / Through all I will be… Lantern

--------------------------------------------------

TRACKS:
1. Lantern
2. Sungai Pagi
3. Lembah Sunyi
4. Pelita
5. Jalan Berliku
6. Fajar
7. Gunung Batu Tinggi
8. Angin Selatan
9. Rumah Kayu
10. Open Skies

Produced & arranged by Andreas Wibisono
© 2017 BSC Worship

Attached files:
1. All Lyrics and Credit Title on PDF and TXT format
2. “Lantern” theme song on MP3 format for your reference
3. BSC Logo (use the round ones). Do not put the logo on the front cover. Use it to incorporate the production info at the back cover only
Updates

Reason: Only received 14 designs. Not so many choices as advertised.

Target Market(s)

Sonora & Playvio Subscribers

Colors

Designer to choose colors to be used in the design.

Requirements
Must have
• Great & eye catching design
Nice to have
• Lantern meaning: Two or more subjects similar to each other
Should not have
• Non-Christian values

```html
<!DOCTYPE html>
<html lang="id">
<head>
<meta charset="utf-8">
<title>Lantern – Insert Sheet</title>
<link href="https://fonts.googleapis.com/css2?family=Oswald:wght@300;400&family=Source+Serif+4:wght@400&family=Source+Sans+3:wght@400&display=swap" rel="stylesheet">
<style>
  :root{
    --board:#cbcbcb;
    --sheet:#f4f4f4;
    --sheet-edge:#e2e2e2;
    --tab:#8b919a;
    --title:#a3a6aa;
    --ink:#1c1c1c;
    --rule:#6f747b;
    --fold-front:#7a7a7a;
    --fold-dark:#3a3a3a;
    --fold-back:#e6e6e6;
  }
  *{margin:0;padding:0;box-sizing:border-box}
  html,body{width:1200px;height:1000px;overflow:hidden;background:var(--board)}
  .board{position:relative;width:1200px;height:1000px}
  .spread{position:absolute;left:30px;top:83px;width:1148px;height:574px;overflow:hidden;
    box-shadow:0 1px 3px rgba(0,0,0,.25)}
  .spread-photo{position:absolute;inset:0;
    background:
      radial-gradient(ellipse at 50% 40%,rgba(255,255,255,.95) 0%,rgba(255,255,255,.6) 45%,rgba(255,255,255,0) 80%),
      linear-gradient(90deg,#e4e4e4 0%,#f6f6f6 20%,#ededed 35%,#f8f8f8 50%,#ececec 65%,#f6f6f6 80%,#e2e2e2 100%)}
  .panel-rule{position:absolute;top:0;width:2px;height:482px;background:var(--rule)}
  .panel{position:absolute;top:0}
  .track-head{position:relative;height:95px;white-space:nowrap}
  .track-tab{position:absolute;left:0;top:0;width:44px;height:95px;background:var(--tab)}
  .track-no,.track-title{position:absolute;top:36px;font-family:'Oswald',sans-serif;font-weight:400;font-size:40px;line-height:48px;letter-spacing:-0.5px}
  .track-no{left:4px;color:#fff}
  .track-title{left:49px;color:var(--title);font-weight:400}
  .writer{font-family:'Source Serif 4',serif;font-size:11.5px;color:var(--ink);margin-top:2px;height:22px}
  .lyrics{font-family:'Oswald',sans-serif;font-weight:300;font-size:12.6px;line-height:18.1px;color:var(--ink);list-style:none}
  .credits{position:absolute;top:401px;font-family:'Oswald',sans-serif;font-weight:300;font-size:7px;line-height:10.3px;color:var(--ink);width:242px}
  .production{position:absolute;top:494px;width:280px;text-align:center;font-family:'Source Serif 4',serif;font-size:9.3px;line-height:12.1px;color:var(--ink)}
  .fold-icon{position:absolute;left:110px;top:700px}
  .label{position:absolute;font-family:'Source Sans 3',sans-serif;font-weight:400;color:#111}
  .label-pages{left:912px;top:700px;font-size:42px}
  .label-fold{left:357px;top:864px;font-size:44px}
</style>
</head>
<body>
<div class="board">
  <section class="spread">
    <div class="spread-photo" role="img" aria-label="Faint white photograph of rows of classical stone columns filling the sheet"></div>

    <div class="panel-rule" style="left:281px"></div>
    <div class="panel-rule" style="left:849px"></div>

    <article class="panel" style="left:23px;width:250px">
      <div class="track-head"><div class="track-tab"></div><span class="track-no">01</span><span class="track-title">LANTERN</span></div>
      <p class="writer">Written by Andreas Wibisono &amp; Rico Halim</p>
      <ul class="lyrics">
        <li>Great is the Lord God almighty</li>
        <li>Your Kingdom come, Your will be done</li>
        <li>Great is the Lord God almighty</li>
        <li>You saved my life, You give me hope</li>
        <li>And through it all</li>
        <li>With all I am</li>
        <li>Lantern... I will shine like You Jesus</li>
        <li>Your love and Your grace live in me</li>
        <li>Lantern... I will live like You Jesus</li>
        <li>Through all I will be Lantern</li>
      </ul>
      <p class="credits" style="left:0">Acoustic Guitars Nadia Putri // Bass Dimas Arya // Cello Laras Wening // Drums Yoga Pratama // Electric Guitars Kevin Lim // Pad Teguh Santika // Piano Bima Nugraha // Violin Sari Melati // Vocals Rina Kusuma / Wulan Sari / Tito Ramli / Mira / Gilang Prasetyo / Rizky Anwar / Shinta Laras</p>
    </article>

    <article class="panel" style="left:302px;width:280px">
      <div class="track-head"><div class="track-tab"></div><span class="track-no">02</span><span class="track-title">SUNGAI PAGI</span></div>
      <p class="writer">Written by Andreas Wibisono</p>
      <ul class="lyrics">
        <li>Written by Andreas Wibisono</li>
        <li>KepadaMu saja diriku berserah</li>
        <li>KuasaMu membelah luas samudra</li>
        <li>Ketika rintangan mulai berbicara</li>
        <li>Kau pun datang segera</li>
        <li>Ketika cintaMu kualami</li>
        <li>Damai terasa dan terbuka langkah surgawi</li>
        <li>Dari Utara, Selatan, Barat, ke Timur</li>
        <li>Ku aman di dalam tanganMu</li>
        <li>Dan ketika cintaMu kualami</li>
        <li>Dalam segalanya Kau mengubah hidup</li>
        <li>Dari Utara, Selatan, Barat, ke Timur</li>
        <li>Ku menikmati hari dalam genggaman tanganMu</li>
      </ul>
      <p class="credits" style="left:0">Bass Dimas Arya // Cello Laras Wening // Drums Yoga Pratama // Electric Guitars Kevin Lim // Violin Sari Melati // Vocals Rina Kusuma / Wulan Sari / Tito Ramli / Mira / Gilang Prasetyo / Rizky Anwar / Shinta Laras</p>
    </article>

    <article class="panel" style="left:593px;width:250px">
      <div class="track-head"><div class="track-tab"></div><span class="track-no">03</span><span class="track-title">LEMBAH SUNYI</span></div>
      <p class="writer">Written by Andreas Wibisono</p>
      <ul class="lyrics">
        <li>Written by Andreas Wibisono</li>
        <li>Di balik segala persoalan</li>
        <li>Ada dalam rancanganNya Tuhan</li>
        <li>Hadapi dengan senyum manismu</li>
        <li>Kau tak pernah sendiri</li>
        <li>Lembah Sunyi</li>
        <li>Lebih dari emas</li>
        <li>Lebih dari takhta</li>
        <li>Lebih dari yang bernafas</li>
        <li>Kasih Yesus sempurna</li>
        <li>Untuk kau dan aku (kita semua)</li>
      </ul>
      <p class="credits" style="left:0">Acoustic Guitars Nadia Putri // Bass Dimas Arya // Drums &amp; Percussions Yoga Pratama // Electric Guitars Kevin Lim // Keys Bima Nugraha // Piano &amp; Strings Dewi Anggraini // Vocals Rina Kusuma / Wulan Sari / Tito Ramli / Mira / Gilang Prasetyo / Rizky Anwar / Shinta Laras</p>
    </article>

    <article class="panel" style="left:872px;width:250px">
      <div class="track-head"><div class="track-tab"></div><span class="track-no">04</span><span class="track-title">PELITA</span></div>
      <p class="writer">Written by Andreas Wibisono</p>
      <ul class="lyrics">
        <li>Di bumi dan di surga</li>
        <li>Kau tetap Rajaku</li>
        <li>Dan kami pun terjaga</li>
        <li>Kau dekap ragaku</li>
        <li>Tuhan.. Pelita</li>
        <li>Roh Kudus besertaku</li>
        <li>Firman.. Mu jadilah</li>
        <li>Penuhi hidupku</li>
      </ul>
      <p class="credits" style="left:0">Bass Dimas Arya // Cello Laras Wening // Drums Yoga Pratama // Electric Guitars Kevin Lim // Violin Sari Melati // Vocals Rina Kusuma / Wulan Sari / Tito Ramli / Mira / Gilang Prasetyo / Rizky Anwar / Shinta Laras</p>
    </article>

    <footer class="production" style="left:95px">
      Recorded by Henry Sulistyo &amp; Maria Sulistyo at Henry Sulistyo Studio<br>
      Mixed by Budiarto<br>
      Mastered by Tonemill Technology<br>
      Produced &amp; arranged by Andreas Wibisono<br>
      © 2017 BSC Worship
    </footer>
    <footer class="production" style="left:723px">
      Recorded by Henry Sulistyo &amp; Maria Sulistyo at Henry Sulistyo Studio<br>
      Mixed by Budiarto<br>
      Mastered by Tonemill Technology<br>
      Produced &amp; arranged by Andreas Wibisono<br>
      © 2017 BSC Worship
    </footer>
  </section>

  <svg class="fold-icon" width="200" height="290" viewBox="0 0 200 290" aria-label="Z-fold diagram">
    <polygon points="52,36 166,6 166,226 52,254" fill="var(--fold-back)"/>
    <polygon points="52,36 166,6 168,12 52,42" fill="#c9c9c9"/>
    <polygon points="17,42 166,36 166,248 17,256" fill="var(--fold-dark)"/>
    <polygon points="17,62 166,60 166,268 17,268" fill="#d4d4d4"/>
    <rect x="5" y="76" width="180" height="202" fill="var(--fold-front)"/>
  </svg>

  <div class="label label-pages">2 first pages</div>
  <div class="label label-fold">z-fold</div>
</div>
</body>
</html>
```